Kestrin Supply Website Redesign

Currently kestrinsupply.example is focussed on fulfillment and transport from various products in the BBQ segment. However, no we want to update our business activities to Product Development, Brand Development, Online Positioning, Logistics & Aftersales, and Promotional BBQs. We will be a business for Outdoor Leisure Development from A to Z.

Therefore, we need a brand new website. The colours of the current website may be the same. However, i'd like to keep it clean. More white and use blue and green as accent colours. It is a business to business organization so the website should be looking formal and corporate. However we sell fun products so not too formal and corporate.

Pages we need; Home, About, Contact, Our Services (+ page per service) a place to share our news/blogs.

I have added some sort of mock up of an idea. However it needs some finetuning.

Businesses

Corporate/Logistics/Marketing

Coded - Design and coding required

Designer to choose colors to be used in the design.

• Show clear distinguishing of the different services we provide (Product Development, Brand Development, Online Positioning, Logistics & Aftersales and Promotional BBQs). Every service should have its own page too. Besides, I would like to have a blog page to share relevant content.
• Show that we are the expert in Outdoor LEisure Development from A to Z
• Be too informal. It may be semi-formal

```html
<!DOCTYPE html>
<html lang="en">
<head>
<meta charset="utf-8">
<title>Kestrin Supply – Outdoor Leisure Development from A to Z</title>
<link rel="stylesheet" href="https://fonts.googleapis.com/css2?family=Open+Sans:wght@400;600;700;800&family=Roboto:wght@400;500;700&display=swap">
<style>
  :root{
    --teal:#4a7585;
    --green:#3fae49;
    --navy:#08083a;
    --ink:#1b1b1b;
    --body:#3a3a3a;
    --light:#f0f0f0;
    --white:#ffffff;
    --head-font:'Open Sans', sans-serif;
    --text-font:'Roboto', sans-serif;
  }
  *{margin:0;padding:0;box-sizing:border-box}
  html,body{width:1200px;height:3092px;overflow:hidden}
  body{position:relative;background:var(--white);font-family:var(--text-font);color:var(--body)}
  .abs{position:absolute}

  /* Header */
  .site-header{position:absolute;left:0;top:0;width:1200px;height:89px;background:var(--white)}
  .brand{position:absolute;left:172px;top:18px;display:flex;align-items:center;gap:12px;font-family:var(--head-font);font-weight:800;font-size:46px;color:var(--teal);letter-spacing:-1px}
  .brand-dot{width:28px;height:28px;border-radius:50%;background:var(--teal)}
  .main-nav a{position:absolute;top:36px;font-family:var(--text-font);font-weight:500;font-size:15px;color:var(--ink);text-decoration:none}
  .nav-home-bg{position:absolute;left:668px;top:4px;width:58px;height:58px;border-radius:50%;background:var(--teal)}
  .nav-home-cap{position:absolute;left:668px;top:0;width:58px;height:22px;border-radius:0 0 29px 29px/0 0 20px 20px;background:var(--green)}
  .main-nav a.is-active{color:var(--white);left:676px}

  /* Hero */
  .hero{position:absolute;left:0;top:89px;width:1200px;height:631px;overflow:hidden;background:#000308}
  .hero-visual{position:absolute;left:0;top:200px;width:1200px;height:520px;
    background:radial-gradient(ellipse 700px 300px at 600px 420px,#49c6e6 0%,#1a6f93 35%,#0b2a45 60%,rgba(0,3,8,0) 80%)}
  .hero-cut{position:absolute;left:0;bottom:0}
  .hero-kicker{position:absolute;top:76px;width:1200px;text-align:center;font-family:var(--head-font);font-weight:600;font-size:34px;color:var(--white)}
  .hero-title{position:absolute;top:118px;width:1200px;text-align:center;font-family:var(--head-font);font-weight:700;font-size:45px;color:var(--white);letter-spacing:.5px}

  /* Service cards */
  .service{position:absolute;top:623px;width:227px;height:313px;background:var(--white);border-radius:8px;overflow:hidden;box-shadow:0 3px 10px rgba(0,0,0,.18);text-align:center}
  .service--featured{height:380px;background:var(--green)}
  .service-badge{position:absolute;left:96px;top:-74px;width:148px;height:148px;border-radius:50%;background:var(--teal)}
  .service-badge--green{background:var(--green)}
  .service--featured .service-badge{background:var(--white)}
  .service-icon{position:absolute;left:138px;top:24px}
  .service h3{position:absolute;top:155px;left:0;width:100%;font-family:var(--text-font);font-weight:500;font-size:17px;color:var(--ink)}
  .service--featured h3,.service--featured p{color:var(--white)}
  .service p{position:absolute;top:185px;left:10px;width:207px;font-size:12.5px;line-height:21px;color:var(--body)}
  .service-more{position:absolute;left:98px;width:31px;height:31px;border-radius:50%;background:var(--teal);display:flex;align-items:center;justify-content:center}
  .service-more--green{background:var(--green)}
  .service--featured .service-more{background:var(--white)}

  /* Difference */
  .difference{position:absolute;left:0;top:1099px;width:1200px;height:511px;overflow:hidden}
  .difference-visual{position:absolute;inset:0;
    background:radial-gradient(ellipse 380px 260px at 1030px 260px,#1f5a62 0%,#0d2a33 50%,rgba(0,0,0,0) 80%),
               linear-gradient(100deg,#03080d 0%,#0a1d27 45%,#05131a 70%,#0c2128 100%)}
  .difference h2{position:absolute;left:172px;top:118px;font-family:var(--head-font);font-weight:700;font-size:35px;color:var(--white)}
  .difference p{position:absolute;left:173px;top:174px;width:478px;font-size:12.5px;line-height:24px;color:var(--white);text-align:justify}
  .btn{position:absolute;left:173px;top:329px;width:101px;height:44px;border-radius:22px;background:var(--green);color:var(--white);font-weight:700;font-size:13.5px;display:flex;align-items:center;justify-content:center;text-decoration:none}
  .disc{position:absolute;border-radius:50%}

  /* News */
  .section-title{position:absolute;width:1200px;text-align:center;font-family:var(--head-font);font-weight:700;font-size:34px;color:var(--teal)}
  .section-title span{color:var(--green)}
  .news-card{position:absolute;top:1765px;width:275px;height:271px;border-radius:36px;overflow:hidden}
  .news-photo{position:absolute;left:0;top:0;width:100%;height:205px}
  .news-label{position:absolute;left:0;top:205px;width:100%;height:66px;display:flex;align-items:center;justify-content:center;font-family:var(--head-font);font-weight:700;font-size:17px;color:var(--white)}
  .news-intro{position:absolute;left:172px;top:2070px;width:856px;text-align:center;font-size:12.5px;line-height:22.5px;color:var(--body)}

  /* Partners */
  .partners{position:absolute;left:0;top:2212px;width:1200px;height:500px;background:var(--light)}
  .partner{position:absolute;top:2380px;width:157px;height:97px;border:1.5px solid #6b6b6b;border-radius:4px;background:var(--white);display:flex;align-items:center;justify-content:center}
  .partner-mark{width:86px;height:30px;border-radius:4px;background:#8c8c8c}

  /* Footer */
  .site-footer{position:absolute;left:0;top:2570px;width:1200px;height:522px}
  .footer-brand{position:absolute;left:0;top:108px;width:1200px;display:flex;justify-content:center;align-items:center;gap:16px;font-family:var(--head-font);font-weight:800;font-size:58px;color:var(--white)}
  .footer-brand .brand-dot{width:34px;height:34px;background:var(--white)}
  .contact-item{position:absolute;top:240px;display:flex;align-items:center;gap:10px;color:var(--white);font-family:var(--head-font);font-size:15.5px;line-height:22px}
  .contact-icon{width:38px;height:38px;border:1.5px solid var(--white);border-radius:50%;display:flex;align-items:center;justify-content:center}
  .footer-nav{position:absolute;left:0;top:356px;width:1200px;display:flex;justify-content:center;gap:32px;font-family:var(--head-font);font-weight:600;font-size:16.5px;color:var(--white)}
  .footer-nav a{color:var(--white);text-decoration:none}
  .footer-rule{position:absolute;left:172px;top:423px;width:856px;height:1px;background:#9a9ab8}
  .copyright{position:absolute;left:0;top:457px;width:1200px;text-align:center;font-family:var(--head-font);font-weight:600;font-size:13.5px;color:var(--white)}
</style>
</head>
<body>

<header class="site-header">
  <div class="brand"><span class="brand-dot"></span>Kestrin</div>
  <nav class="main-nav">
    <span class="nav-home-bg"></span>
    <span class="nav-home-cap"></span>
    <a class="is-active" href="#">HOME</a>
    <a href="#" style="left:749px">ABOUT</a>
    <a href="#" style="left:828px">OUR SERVICES</a>
    <a href="#" style="left:959px">CONTACT</a>
  </nav>
</header>

<section class="hero">
  <div class="hero-visual" role="img" aria-label="Glowing earth horizon with network arcs linking locations worldwide"></div>
  <svg class="hero-cut" width="1200" height="140" viewBox="0 0 1200 140" aria-hidden="true">
    <path d="M0,118 Q600,20 1200,118 L1200,140 L0,140 Z" fill="#ffffff"/>
  </svg>
  <div class="hero-kicker">OUTDOOR LEISURE</div>
  <h1 class="hero-title">DEVELOPMENT FROM A TO Z</h1>
</section>

<article class="service" style="left:127px">
  <span class="service-badge"></span>
  <svg class="service-icon" width="62" height="56" viewBox="0 0 62 56" fill="none" stroke="#fff" stroke-width="3">
    <path d="M6 18 L24 10 L40 18 L40 40 L24 48 L6 40 Z"/><circle cx="40" cy="22" r="11" fill="#4a7585"/><line x1="48" y1="30" x2="58" y2="40"/>
  </svg>
  <h3>PRODUCT DEVELOPMENT</h3>
  <p>We believe that the partners we work for should be able to focus on building their brand and product.</p>
  <span class="service-more" style="top:264px"><svg width="14" height="14" viewBox="0 0 14 14"><path d="M3 5 L7 9 L11 5" stroke="#fff" stroke-width="2" fill="none"/></svg></span>
</article>

<article class="service service--featured" style="left:367px">
  <span class="service-badge"></span>
  <svg class="service-icon" width="56" height="56" viewBox="0 0 56 56" fill="none" stroke="#3fae49" stroke-width="3">
    <path d="M8 20 L14 6 L42 6 L48 20 Z"/><path d="M8 20 Q14 28 20 20 Q28 28 36 20 Q42 28 48 20"/><rect x="11" y="26" width="34" height="24"/><rect x="20" y="34" width="16" height="10"/>
  </svg>
  <h3>BRAND DEVELOPMENT</h3>
  <p>We believe that the partners we work for should be able to focus on building their brand and product. Kestrin distribu tion therefore takes care of the process from order processing to delivery. Together with our Partner Kestrin Promotional.</p>
  <span class="service-more" style="top:337px"><svg width="14" height="14" viewBox="0 0 14 14"><path d="M3 5 L7 9 L11 5" stroke="#3fae49" stroke-width="2" fill="none"/></svg></span>
</article>

<article class="service" style="left:607px">
  <span class="service-badge"></span>
  <svg class="service-icon" width="60" height="56" viewBox="0 0 60 56" fill="none" stroke="#fff" stroke-width="3">
    <rect x="6" y="20" width="44" height="26"/><line x1="2" y1="50" x2="54" y2="50"/><path d="M30 22 L44 14 L44 32 Z"/><line x1="50" y1="10" x2="56" y2="6"/>
  </svg>
  <h3>ONLINE POSITIONING</h3>
  <p>We believe that the partners we work for should be able to focus on building their brand and product.</p>
  <span class="service-more" style="top:264px"><svg width="14" height="14" viewBox="0 0 14 14"><path d="M3 5 L7 9 L11 5" stroke="#fff" stroke-width="2" fill="none"/></svg></span>
</article>

<article class="service" style="left:847px">
  <span class="service-badge service-badge--green"></span>
  <svg class="service-icon" width="68" height="56" viewBox="0 0 68 56" fill="none" stroke="#fff" stroke-width="3">
    <path d="M6 42 L6 26 L16 26 L22 12 L34 12 L34 42 Z"/><circle cx="12" cy="44" r="5"/><circle cx="30" cy="44" r="5"/><line x1="40" y1="6" x2="40" y2="46"/><rect x="48" y="14" width="12" height="12"/><rect x="48" y="30" width="12" height="12"/>
  </svg>
  <h3>LOGISTICS &amp; AFTERSALES</h3>
  <p>We believe that the partners we work for should be able to focus on building their brand and product.</p>
  <span class="service-more service-more--green" style="top:264px"><svg width="14" height="14" viewBox="0 0 14 14"><path d="M3 5 L7 9 L11 5" stroke="#fff" stroke-width="2" fill="none"/></svg></span>
</article>

<section class="difference">
  <div class="difference-visual" role="img" aria-label="Dark warehouse scene with a forklift, parcels and a laptop overlaid with a glowing world network"></div>
  <h2>WE MAKE THE DIFFERENCE</h2>
  <p>We believe that the partners we work for should be able to focus on building their brand and product. Kestrin distribution therefore takes care of the process from order processing to delivery. Together with our Partner Kestrin Promotional, we can also provide support in the commercial process. We have supplier relationships in more than 30 countries in both the retail and promotional products market.</p>
  <a class="btn" href="#">Read More</a>
  <span class="disc" style="left:766px;top:61px;width:260px;height:260px;background:var(--green)"></span>
  <span class="disc" style="left:766px;top:192px;width:260px;height:260px;background:var(--teal)"></span>
</section>

<h2 class="section-title" style="top:1680px">LATEST <span>NEWS</span></h2>

<article class="news-card" style="left:173px">
  <div class="news-photo" role="img" aria-label="Businessman on a rooftop overlooking a connected city skyline at dusk" style="background:linear-gradient(180deg,#2d4f78 0%,#5b7fa8 45%,#1c3552 100%)"></div>
  <div class="news-label" style="background:var(--teal)">PROJECT DISTRIBUTION</div>
</article>
<article class="news-card" style="left:462px">
  <div class="news-photo" role="img" aria-label="Businesswoman walking through a modern glass office corridor" style="background:linear-gradient(90deg,#2b4a63 0%,#7f99ab 40%,#3d3a3a 70%,#6a6560 100%)"></div>
  <div class="news-label" style="background:var(--green)">FULFILLMENT</div>
</article>
<article class="news-card" style="left:751px">
  <div class="news-photo" role="img" aria-label="Two colleagues packing parcels in a small warehouse office" style="background:linear-gradient(135deg,#6b5a4a 0%,#b8a48a 50%,#d9cbb5 100%)"></div>
  <div class="news-label" style="background:var(--teal)">LOYALTY PROGRAMS</div>
</article>

<p class="news-intro">We believe that the partners we work for should be able to focus on building their brand and product. Kestrin distribution therefore takes care of the process from order processing to delivery. Together with our Partner Kestrin Promotional, we can also provide support in the commercial process. We have supplier relationships in more than 30 countries in both the retail and promotional products market.</p>

<section class="partners">
  <h2 class="section-title" style="top:78px">OUR <span>PARTNERS</span></h2>
</section>
<div class="partner" style="left:173px"><span class="partner-mark"></span></div>
<div class="partner" style="left:347px"><span class="partner-mark"></span></div>
<div class="partner" style="left:521px"><span class="partner-mark"></span></div>
<div class="partner" style="left:695px"><span class="partner-mark"></span></div>
<div class="partner" style="left:869px"><span class="partner-mark"></span></div>

<footer class="site-footer">
  <svg class="abs" style="left:0;top:0" width="1200" height="522" viewBox="0 0 1200 522" aria-hidden="true">
    <path d="M0,70 Q600,-50 1200,70 L1200,522 L0,522 Z" fill="#08083a"/>
  </svg>
  <div class="footer-brand"><span class="brand-dot"></span>Kestrin</div>

  <div class="contact-item" style="left:172px">
    <span class="contact-icon"><svg width="18" height="20" viewBox="0 0 18 20" fill="none" stroke="#fff" stroke-width="1.6"><path d="M9 19 C3 12 2 9 2 7 A7 7 0 0 1 16 7 C16 9 15 12 9 19 Z"/><circle cx="9" cy="7" r="2.5"/></svg></span>
    <span>Harbourline 12,<br>4100 KS Elmsworth</span>
  </div>
  <div class="contact-item" style="left:524px">
    <span class="contact-icon"><svg width="18" height="18" viewBox="0 0 18 18" fill="none" stroke="#fff" stroke-width="1.6"><path d="M4 2 L7 2 L8 6 L6 7.5 Q7.5 10.5 10.5 12 L12 10 L16 11 L16 14 Q16 16 14 16 Q3 15 2 4 Q2 2 4 2 Z"/></svg></span>
    <span>Elmsworth Office:<br>+31 (0)10 555 0142</span>
  </div>
  <div class="contact-item" style="left:798px">
    <span class="contact-icon"><svg width="20" height="14" viewBox="0 0 20 14" fill="none" stroke="#fff" stroke-width="1.6"><rect x="1" y="1" width="18" height="12"/><path d="M1 1 L10 8 L19 1"/></svg></span>
    <span>Mail:<br>info@kestrinsupply.example</span>
  </div>

  <nav class="footer-nav">
    <a href="#">HOME</a><span>|</span><a href="#">ABOUT</a><span>|</span><a href="#">OUR SERVICES</a><span>|</span><a href="#">CONTACT</a><span>|</span><a href="#">BLOG</a>
  </nav>
  <div class="footer-rule"></div>
  <p class="copyright">Copyrights @ 2021 Kestrin. All Rights Reserved.</p>
</footer>

</body>
</html>
```